Label design for loose leaf tea pouches and tins

Starting my loose leaf tea business and looking for product labels.
I already have logo designed and would love it to be worked into the label;
Label sizes and sample text is in the attachments;
Pouches and tins pictures are also in the attachments.

looking for the recommendation on what is the best color for the pouch.
Updates

Here is the link: https://docs.plumbrix.com/spreadsheets/d/7kTq2wLm9PzX4vHc8RnYb3JdFs6GaUe1QoWt5NyKx2Ze/edit

Adding the pdf since plumbrix links do not work here

Target Market(s)

Women and men, 35+, USA

Font styles to use
Serif

Requirements
Must have
• Front and back label

```html
<!DOCTYPE html>
<html lang="en">
<head>
<meta charset="utf-8">
<title>Rooibos – Front and Back Tea Labels</title>
<link rel="stylesheet" href="https://fonts.googleapis.com/css2?family=Alegreya:ital,wght@1,700&family=Quattrocento:wght@400;700&display=swap">
<style>
  :root {
    --canvas: #ffffff;
    --charcoal: #363636;
    --panel: #ffffff;
    --ink: #333333;
    --ornament-dark: #3b3b3b;
    --ornament-light: #e6e6e6;
    --leaf-green: #8a9a3c;
    --leaf-stem: #a27a3c;
    --saffron: #f7b232;
    --shadow: rgba(0, 0, 0, 0.35);
  }

  * { box-sizing: border-box; margin: 0; padding: 0; }

  html, body {
    width: 1200px;
    height: 739px;
    overflow: hidden;
    background: var(--canvas);
  }

  .label-sheet {
    position: relative;
    width: 1200px;
    height: 739px;
    font-family: "Quattrocento", Georgia, serif;
    color: var(--ink);
  }

  .label {
    position: absolute;
    top: 78px;
    width: 410px;
    height: 558px;
    background: var(--charcoal);
    box-shadow: 4px 5px 9px var(--shadow);
    overflow: hidden;
  }

  .label--front { left: 170px; }
  .label--back  { left: 596px; }

  .label__panel {
    position: absolute;
    background: var(--panel);
    bottom: 0;
  }

  .label--front .label__panel { left: 44px; width: 334px; top: 93px; }
  .label--back .label__panel  { left: 36px; width: 333px; top: 137px; }

  /* Front label */
  .front-ornament {
    position: absolute;
    left: 28px;
    top: 0;
    width: 350px;
    height: 182px;
    background: radial-gradient(ellipse at 50% 20%, #4a4a4a 0%, var(--ornament-dark) 70%);
    border-radius: 0 0 50% 50% / 0 0 100% 100%;
  }

  .product-name {
    position: absolute;
    left: 0;
    width: 100%;
    top: 196px;
    text-align: center;
    font-family: "Alegreya", Georgia, serif;
    font-style: italic;
    font-weight: 700;
    font-size: 50px;
    line-height: 1;
    color: var(--ink);
  }

  .herb-illustration {
    position: absolute;
    left: 175px;
    top: 256px;
    width: 60px;
    height: 126px;
    background: linear-gradient(180deg, #d9d24a 0%, var(--leaf-green) 30%, var(--leaf-green) 75%, var(--leaf-stem) 100%);
    border-radius: 45% 45% 20% 20%;
  }

  .tagline {
    position: absolute;
    left: 0;
    width: 100%;
    top: 390px;
    text-align: center;
    font-size: 15px;
    line-height: 19px;
  }

  .pack-detail {
    position: absolute;
    font-size: 12px;
    line-height: 14px;
  }

  .pack-detail--servings { left: 64px; top: 516px; }
  .pack-detail--weight   { left: 276px; top: 530px; }

  .brand-mark {
    position: absolute;
    left: 0;
    width: 100%;
    top: 526px;
    display: flex;
    justify-content: center;
    align-items: center;
    gap: 6px;
  }

  .brand-mark__dot {
    width: 14px;
    height: 14px;
    border-radius: 50%;
    background: var(--saffron);
  }

  .brand-mark__name {
    font-family: "Quattrocento", Georgia, serif;
    font-weight: 700;
    font-size: 14px;
    letter-spacing: 1px;
    color: var(--ink);
  }

  /* Back label */
  .description {
    position: absolute;
    left: 36px;
    width: 333px;
    top: 160px;
    text-align: center;
    font-size: 14px;
    line-height: 16.5px;
  }

  .origin {
    position: absolute;
    left: 62px;
    top: 346px;
    font-size: 11px;
    line-height: 13px;
    z-index: 2;
  }

  .back-ornament {
    position: absolute;
    left: 6px;
    top: 400px;
    width: 395px;
    height: 158px;
    background: radial-gradient(ellipse at 50% 100%, var(--ornament-light) 0%, #f4f4f4 60%, #dcdcdc 100%);
    border: 1.5px solid #555555;
    border-bottom: none;
    border-radius: 50% 50% 0 0 / 100% 100% 0 0;
  }
</style>
</head>
<body>
<main class="label-sheet">

  <section class="label label--front" aria-label="Front label">
    <div class="label__panel"></div>
    <div class="front-ornament" role="img" aria-label="Dark mandala ornament hanging from the top edge"></div>
    <h1 class="product-name">Rooibos</h1>
    <div class="herb-illustration" role="img" aria-label="Illustration of a rooibos sprig with a small yellow flower"></div>
    <p class="tagline">Delicious concoction of Indian herbs<br>and flowers to help you slow down<br>and unwind</p>
    <p class="pack-detail pack-detail--servings">50 servings<br>Decaffinate</p>
    <div class="brand-mark">
      <span class="brand-mark__dot"></span>
      <span class="brand-mark__name">STEEP HOUR</span>
    </div>
    <p class="pack-detail pack-detail--weight">3.4 OZ / 100g</p>
  </section>

  <section class="label label--back" aria-label="Back label">
    <div class="label__panel"></div>
    <p class="description">Truly magic wellness potion<br>formulated with combination of &nbsp; worldclass<br>ingridients. Ease Up tea calms you down,<br>warms you up, eases anxiety and fights signs<br>of depression.<br>Turmeric, cardamom and ginger reduce<br>symptoms of gas and<br>bloating and facilitate digestion</p>
    <div class="back-ornament" role="img" aria-label="Light outlined mandala ornament rising from the bottom edge"></div>
    <p class="origin">Country of origin:<br>India<br>Loose Leaf Tea</p>
  </section>

</main>
</body>
</html>
```